KAV cards & more
Business cards, fax cover sheet, letterhead, envelopes, powerpoint slide template
Modern
Tad Willers
Owner
17 Lindgate Row Hollin Falls, ST 00482
twkav@mailvane.net
Please integrate my already-completed company logo (attached) in a clean, modern design for business cards, Fax cover sheet, letterhead, envelopes, and powerpoint slide template

```html
<!DOCTYPE html>
<html lang="en">
<head>
<meta charset="utf-8">
<title>KAV Business Card</title>
<link rel="stylesheet" href="https://fonts.googleapis.com/css2?family=Montserrat:wght@400;600;800&display=swap">
<style>
  :root {
    --bg: #ecece8;
    --green-dark: #0d6a2a;
    --green: #1f8a34;
    --green-light: #52b545;
    --lime: #9fd04a;
    --ink: #4a4a4a;
    --white: #ffffff;
  }
  * { margin: 0; padding: 0; box-sizing: border-box; }
  html, body {
    width: 1200px; height: 1030px; overflow: hidden;
    background: var(--bg);
    font-family: "Montserrat", Arial, sans-serif;
  }
  .sheet {
    width: 1200px; height: 1030px;
    display: flex; flex-direction: column; align-items: center; justify-content: center;
    gap: 80px;
  }
  .card {
    position: relative; width: 700px; height: 400px; overflow: hidden;
    box-shadow: 0 10px 28px rgba(0,0,0,.22);
  }
  .card-front { background: var(--white); }
  .front-art { position: absolute; inset: 0; }
  .holder { position: absolute; top: 34px; right: 40px; text-align: right; color: var(--white); }
  .holder-name { font-weight: 800; font-size: 26px; letter-spacing: .3px; }
  .holder-title { font-weight: 400; font-size: 14px; margin-top: 4px; }
  .brand { position: absolute; left: 40px; top: 198px; display: flex; align-items: center; gap: 16px; }
  .brand-dot { width: 54px; height: 54px; border-radius: 50%; background: var(--green-light); }
  .brand-name { font-weight: 800; font-size: 52px; color: var(--green); letter-spacing: 4px; line-height: 1; }
  .contact { position: absolute; left: 40px; bottom: 30px; font-size: 13px; font-style: normal; color: var(--ink); line-height: 1.6; }
  .contact b { color: var(--green); font-weight: 600; }
  .card-back {
    background: radial-gradient(ellipse at 50% 30%, var(--green-light) 0%, var(--green) 45%, var(--green-dark) 100%);
    display: flex; align-items: center; justify-content: center;
  }
  .back-brand { font-weight: 800; font-size: 72px; color: var(--white); letter-spacing: 6px; }
</style>
</head>
<body>
<main class="sheet">
  <section class="card card-front">
    <svg class="front-art" width="700" height="400" viewBox="0 0 700 400" aria-hidden="true">
      <defs>
        <linearGradient id="bandFill" x1="0" y1="0" x2="1" y2="0">
          <stop offset="0" stop-color="#1f8a34"/>
          <stop offset="1" stop-color="#0d6a2a"/>
        </linearGradient>
      </defs>
      <path d="M0,0 H700 V120 C500,110 240,120 0,190 Z" fill="url(#bandFill)"/>
      <path d="M0,190 C240,120 500,110 700,120" fill="none" stroke="#9fd04a" stroke-width="7"/>
    </svg>
    <div class="holder">
      <div class="holder-name">Tad Willers</div>
      <div class="holder-title">Owner</div>
    </div>
    <div class="brand">
      <span class="brand-dot"></span>
      <span class="brand-name">KAV</span>
    </div>
    <address class="contact">
      <div>17 Lindgate Row Hollin Falls, ST 00482</div>
      <div><b>C:</b> 555 014 0142 &nbsp;<b>F:</b> 555 014 0187</div>
      <div><b>E:</b> twkav@mailvane.net</div>
    </address>
  </section>

  <section class="card card-back">
    <span class="back-brand">KAV</span>
  </section>
</main>
</body>
</html>
```